Flyer for Custom Home Builder!

my company is Harlow Ridge Homes, I am looking for a flyer that we can send via email to a customer, or print and hand out. I am thinking four pages so we could print this and fold it., possibly creating a folder. The name of the company is Harlow Ridge Homes our website is here www.harlowridgehomes-example.com. Some text you can use "Crafting luxury homes isn't just a job, it's our passion.
With meticulous attention to detail and an unwavering commitment to using the finest materials, Harlow Ridge Homes consistently delivers exceptional results that stand as a testament to our commitment to quality."

"Trust is the cornerstone of our foundation.
With a proven track record of delivering on our promises for over 16 years, we prioritize transparent communication and integrity throughout every step of the home-building journey".

you may need to obtain the photos here
https://files.example-share.net/f/k27pw4m8zrt03xq61bnv/h?key=48vn2c9q1x7mb5t0ekd3h&dl=0

Target Market(s)

We build homes for every wealthy clients, therefore the photos are extremely important

Industry/Entity Type

Construction.

Requirements
Must have
• clear larger photos

```html
<!DOCTYPE html>
<html lang="en">
<head>
<meta charset="utf-8">
<title>Harlow Ridge Homes – Brochure</title>
<link rel="stylesheet" href="https://fonts.googleapis.com/css2?family=Cinzel:wght@400;600&family=Roboto:wght@400;500;700&display=swap">
<style>
  :root {
    --canvas: #e6e6e6;
    --page-grey: #bdbdbd;
    --page-grey-light: #c6c6c6;
    --cream: #ebe8e2;
    --ink: #111111;
    --ink-soft: #2b2b2b;
    --white: #ffffff;
    --logo-ink: #3c3c3c;
    --logo-plate: #dcdcdc;
    --dusk-top: #4a4a66;
    --dusk-mid: #8a6f86;
    --house-dark: #3b3a40;
    --photo-warm: #7d6d66;
    --photo-sky: #c88fb6;
    --photo-blue: #7fa3c0;
    --photo-wood: #8a6a4c;
  }
  * { margin: 0; padding: 0; box-sizing: border-box; }
  html, body {
    width: 1200px; height: 3000px; overflow: hidden;
    background: var(--canvas);
  }
  .spread-frame {
    position: absolute; left: 50px; width: 1100px; height: 690px;
    box-shadow: 0 6px 18px rgba(0,0,0,.25);
  }
  .spread-frame.outer { top: 760px; }
  .spread-frame.inner { top: 1550px; }
  .spread {
    position: absolute; left: 0; top: 0; width: 900px; height: 565px;
    transform: scale(1.22222); transform-origin: 0 0;
    background: var(--page-grey); overflow: hidden;
  }
  .spread > svg.shapes { position: absolute; left: 0; top: 0; }

  .wordmark {
    position: absolute; background: var(--logo-plate);
    padding: 4px 8px; text-align: center;
    font-family: "Roboto", sans-serif; font-weight: 700;
    color: var(--logo-ink); letter-spacing: 2px; line-height: 1.05;
    text-transform: uppercase;
  }

  /* Outer spread */
  .cover-wordmark { left: 655px; top: 26px; font-size: 15px; width: 162px; }
  .back-wordmark { left: 88px; top: 370px; font-size: 14px; width: 156px; }
  .cover-title {
    position: absolute; left: 480px; top: 360px; width: 420px; text-align: center;
    color: var(--white); font-family: "Cinzel", serif;
  }
  .cover-title h1 { font-size: 25px; font-weight: 400; letter-spacing: 1px; }
  .cover-title p { font-size: 14px; letter-spacing: 1px; margin-top: 10px; }
  .cover-intro {
    position: absolute; left: 500px; top: 456px; width: 360px; text-align: center;
    font-family: "Roboto", sans-serif; font-weight: 500; font-size: 11px; line-height: 1.65;
    color: var(--ink-soft);
  }
  .contact { position: absolute; left: 33px; top: 427px; font-family: "Roboto", sans-serif; color: var(--ink); }
  .contact h2 { font-size: 14px; font-weight: 500; margin-bottom: 8px; }
  .contact ul { list-style: none; }
  .contact li { display: flex; align-items: center; gap: 10px; font-size: 9px; height: 22px; }
  .contact li svg { flex: none; }

  /* Inner spread – left page text wraps along the diagonal stripes */
  .stripe-wrap {
    position: absolute; left: 0; top: 0; width: 432px; height: 565px;
    display: flow-root; font-family: "Cinzel", serif; color: var(--ink);
    text-align: right;
  }
  .stripe-edge {
    float: left; width: 322px; height: 565px;
    shape-outside: polygon(0 0, 322px 0, 132px 565px, 0 565px);
  }
  .advocates h2 { font-size: 15px; font-weight: 400; line-height: 1.1; margin: 18px 0 14px; }
  .advocates p {
    font-size: 6.6px; line-height: 1.32; margin-bottom: 9px; text-transform: uppercase;
  }
  .team h2 { font-size: 14px; font-weight: 400; line-height: 1.1; margin: 352px 0 10px; }
  .team p { font-size: 6.6px; line-height: 1.32; text-transform: uppercase; }
  .inner-wordmark { left: 296px; top: 512px; font-size: 13px; width: 130px; }

  .about {
    position: absolute; left: 468px; top: 276px; width: 410px;
    font-family: "Roboto", sans-serif; color: var(--ink);
  }
  .about h2 { font-family: "Cinzel", serif; font-size: 15px; font-weight: 400; margin-bottom: 8px; }
  .about p { font-size: 9.2px; line-height: 1.4; text-align: justify; }
  .about h3 {
    font-size: 12.5px; font-weight: 400; letter-spacing: 1.5px; text-align: justify;
    text-align-last: left; line-height: 1.35; margin: 12px 0 8px;
  }
</style>
</head>
<body>

<section class="spread-frame outer">
  <div class="spread">
    <svg class="shapes" width="900" height="565" viewBox="0 0 900 565">
      <defs>
        <linearGradient id="backPhoto" x1="0" y1="0" x2="0" y2="1">
          <stop offset="0" stop-color="var(--dusk-top)"/>
          <stop offset=".35" stop-color="var(--dusk-mid)"/>
          <stop offset=".55" stop-color="var(--photo-warm)"/>
          <stop offset="1" stop-color="var(--house-dark)"/>
        </linearGradient>
        <linearGradient id="coverPhoto" x1="0" y1="0" x2="0" y2="1">
          <stop offset="0" stop-color="var(--photo-sky)"/>
          <stop offset=".35" stop-color="#d8cdc3"/>
          <stop offset=".75" stop-color="#8c7f74"/>
          <stop offset="1" stop-color="#5b534d"/>
        </linearGradient>
      </defs>
      <polygon points="0,0 430,0 345,340 0,340" fill="url(#backPhoto)" role="img" aria-label="Photo of a Mediterranean-style luxury home at dusk"/>
      <polygon points="430,0 900,0 900,80 410,80" fill="var(--cream)"/>
      <path d="M0,330 L275,330 Q300,330 300,355 L310,565 L0,565 Z" fill="var(--cream)"/>
      <polygon points="410,80 900,80 900,335 335,335" fill="var(--white)"/>
      <polygon points="413,84 900,84 900,331 340,331" fill="url(#coverPhoto)" role="img" aria-label="Photo of a modern two-storey stone luxury home at sunset"/>
      <polygon points="318,345 345,345 322,440 295,440" fill="var(--ink)"/>
      <polygon points="357,345 384,345 361,440 334,440" fill="var(--ink)"/>
      <polygon points="396,345 423,345 400,440 373,440" fill="var(--ink)"/>
      <polygon points="435,345 900,345 900,440 412,440" fill="var(--ink)"/>
    </svg>

    <div class="wordmark cover-wordmark">Harlow Ridge<br>Homes</div>
    <div class="cover-title">
      <h1>CRAFTING LUXURY HOMES</h1>
      <p>ISN'T JUST A JOB, IT'S OUR PASSION.</p>
    </div>
    <p class="cover-intro">With meticulous attention to detail and an unwavering commitment to using the finest materials, Harlow Ridge Homes consistently delivers exceptional results that stand as a testament to our commitment to quality.</p>

    <div class="wordmark back-wordmark">Harlow Ridge<br>Homes</div>
    <div class="contact">
      <h2>Harlow Ridge Homes</h2>
      <ul>
        <li><svg width="18" height="18" viewBox="0 0 18 18"><circle cx="9" cy="9" r="8" fill="none" stroke="#222" stroke-width="1"/><path d="M6 5 L7.5 5 L8.3 7 L7.3 7.8 Q8 9.8 10.2 10.8 L11 9.8 L13 10.6 L13 12 Q11.5 13.2 9.5 12.2 Q6 10.5 5.2 6.5 Z" fill="none" stroke="#222" stroke-width=".9"/></svg>(512) 555-0147</li>
        <li><svg width="18" height="18" viewBox="0 0 18 18"><circle cx="9" cy="9" r="8" fill="none" stroke="#222" stroke-width="1"/><rect x="5" y="6" width="8" height="6" fill="none" stroke="#222" stroke-width=".9"/><path d="M5 6 L9 9.5 L13 6" fill="none" stroke="#222" stroke-width=".9"/></svg>INFO@HARLOWRIDGEHOMES-EXAMPLE.COM</li>
        <li><svg width="18" height="18" viewBox="0 0 18 18"><circle cx="9" cy="9" r="8" fill="none" stroke="#222" stroke-width="1"/><circle cx="9" cy="9" r="4.5" fill="none" stroke="#222" stroke-width=".9"/><ellipse cx="9" cy="9" rx="2" ry="4.5" fill="none" stroke="#222" stroke-width=".9"/><line x1="4.5" y1="9" x2="13.5" y2="9" stroke="#222" stroke-width=".9"/></svg>www.harlowridgehomes-example.com</li>
        <li><svg width="18" height="18" viewBox="0 0 18 18"><circle cx="9" cy="9" r="8" fill="none" stroke="#222" stroke-width="1"/><path d="M9 13.5 Q5.5 9.5 5.5 7.5 A3.5 3.5 0 0 1 12.5 7.5 Q12.5 9.5 9 13.5 Z" fill="none" stroke="#222" stroke-width=".9"/><circle cx="9" cy="7.5" r="1.2" fill="#222"/></svg><span>4820 CEDAR BLUFF LANE,<br>SUITE 210, AUSTIN TX 78730</span></li>
      </ul>
    </div>
  </div>
</section>

<section class="spread-frame inner">
  <div class="spread">
    <svg class="shapes" width="900" height="565" viewBox="0 0 900 565">
      <defs>
        <linearGradient id="poolPhoto" x1="0" y1="0" x2="0" y2="1">
          <stop offset="0" stop-color="var(--photo-blue)"/>
          <stop offset=".2" stop-color="#e8e6e2"/>
          <stop offset=".3" stop-color="var(--photo-wood)"/>
          <stop offset=".55" stop-color="#5e6a66"/>
          <stop offset=".8" stop-color="#4fa3b8"/>
          <stop offset="1" stop-color="#3f5560"/>
        </linearGradient>
        <linearGradient id="patioPhoto" x1="0" y1="0" x2="0" y2="1">
          <stop offset="0" stop-color="var(--photo-sky)"/>
          <stop offset=".4" stop-color="#7c746c"/>
          <stop offset=".75" stop-color="#9a9590"/>
          <stop offset="1" stop-color="#5c5751"/>
        </linearGradient>
      </defs>
      <rect x="0" y="0" width="450" height="565" fill="var(--page-grey-light)"/>
      <polygon points="0,0 215,0 25,565 0,565" fill="url(#poolPhoto)" role="img" aria-label="Photo of a modern home terrace with pool and lounge seating"/>
      <polygon points="215,0 245,0 55,565 25,565" fill="var(--ink)"/>
      <polygon points="245,0 254,0 64,565 55,565" fill="var(--white)"/>
      <polygon points="254,0 275,0 85,565 64,565" fill="var(--ink)"/>
      <polygon points="275,0 286,0 96,565 85,565" fill="var(--white)"/>
      <polygon points="286,0 308,0 118,565 96,565" fill="var(--ink)"/>

      <polygon points="450,232 900,232 900,246 450,246" fill="var(--ink)"/>
      <polygon points="490,0 520,0 465,232 450,232 450,170" fill="var(--ink)"/>
      <polygon points="530,0 560,0 505,232 475,232" fill="var(--ink)"/>
      <polygon points="570,0 600,0 545,232 515,232" fill="var(--ink)"/>
      <polygon points="612,0 900,0 900,226 558,226" fill="url(#patioPhoto)" role="img" aria-label="Photo of an outdoor living area with fire pit and seating at dusk"/>
      <polygon points="558,226 900,226 900,232 557,232" fill="var(--white)"/>
      <rect x="450" y="555" width="450" height="10" fill="var(--white)"/>
    </svg>

    <div class="stripe-wrap advocates">
      <div class="stripe-edge"></div>
      <h2>WE WANT TO<br>BE YOUR AD-<br>VOCATES AND<br>LONG-TERM<br>PARTNERS.</h2>
      <p>At Harlow Ridge Homes, we understand that building a custom home is a significant investment, both financially and emotionally. That is why we are committed to being your advocates every step of the way.</p>
      <p>From the initial design consultation to the final walk-through, we will be there to guide you through the entire process, answering any question you may have. We ensure that your vision is brought to life. Our team of experienced professionals is dedicated to providing exceptional service and craftsmanship, and we take pride in building long-lasting relationships with clients.</p>
      <p>When you choose Harlow Ridge Homes, you can rest assured that you will have a team of passionate advocates on your side, working tirelessly to create a home that you will cherish for years to come.</p>
    </div>

    <div class="stripe-wrap team">
      <div class="stripe-edge"></div>
      <h2>YOU DON'T JUST HAVE ONE<br>PERSON IN YOUR COR-<br>NER—YOU HAVE MANY.</h2>
      <p>Our team-based approach makes it so everyone, from our owners to our subcontractors, works toward the same goal: to build your ideal property. You entrusting us with creating your dream home is an honor and responsibility we don't take lightly, so we infuse passion and care into everything we do. Rest assured that your best interest is our focus and is at the heart of every decision we make, down to the smallest detail.</p>
    </div>
    <div class="wordmark inner-wordmark">Harlow Ridge Homes</div>

    <div class="about">
      <h2>HARLOW RIDGE HOMES</h2>
      <p>Harlow Ridge Homes is a premier custom home builder committed to creating exceptional, one-of-a-kind homes that reflect the unique vision and style of our clients. With over two decades of experience in the industry, we have earned a reputation for unparalleled craftsmanship and attention to detail, resulting in homes that are both luxurious and functional. We work closely with our clients from start to finish to ensure that every detail is carefully considered and executed to perfection, resulting in homes that exceed our clients' expectations. At Harlow Ridge Homes, we believe in creating homes that are as individual as our clients, and we are dedicated to providing exceptional service and quality craftsmanship to every project we take on.</p>
      <h3>WE CAN CREATE AN ARCHITECTURAL MARVEL THAT PERFECTLY SUITS YOUR NEEDS AND DESIRES.</h3>
      <p>Whether you want a technological utopia equipped with the latest amenities or a stunning country estate tucked away in unspoiled natural scenery, a rustic ranch enjoying views of the rolling hillside or a chateau with easy access to Lake Travis.</p>
    </div>
  </div>
</section>

</body>
</html>
```